Lumaform website scandinavian interior design

Existing website: http://lumaform-example.no/

Webdesign for interior designer Ragna Tvedtholm. The company name is Lumaform. Scandinavian interiør is known to be simple and elegant. The website will be in Norwegian, we are working on the text. The website needs to have a few more pages than just the front page. Here are the different titles of the pages:

1. Hjem
2. Om Lumaform
3. Tjenester og priser
4.. Kontakt oss

There should be Facebook and Instagram icons somewhere at the bottom of the website.

The logo we want to use is attached (pink with black print, see attachment )

We have attached images for inspiration. We want to use some of these colors. The color in the logo, The style should be elegant, modern and delicate.

It is imprtant that the website is user friendly.

Target Market(s)

People who want to decorate their home
Companies and public sector who need to redecorate

Industry/Entity Type

Interior Designer

Coding

Coded - Design and coding required

Number of Pages Required

5+ page

Font styles to use
Other font styles liked:
• see example in the logo breakdown

Requirements
Must have
• Elegant, modern and delicate design
Images of design, see examples attached
Colors similar to the pictures
Should not have
• Too bright colors
Pictures of people

```html
<!DOCTYPE html>
<html lang="en">
<head>
<meta charset="utf-8">
<title>Lumaform – Scandinavian Interior Design</title>
<link href="https://fonts.googleapis.com/css2?family=PT+Serif&family=Space+Mono&display=swap" rel="stylesheet">
<style>
:root{
  --bg:#f7e8e4;
  --white:#ffffff;
  --ink:#2f2424;
  --ink-soft:#4a3c3c;
  --line:#6d5a5a;
  --accent:#5c3434;
  --hero-a:#8d8b8c;
  --hero-b:#b3b1b2;
  --dots:#3a2c2c;
}
*{box-sizing:border-box;margin:0;padding:0}
html,body{width:1200px;height:3445px;overflow:hidden}
body{background:var(--bg);color:var(--ink);font-family:"Space Mono",monospace;position:relative}
.abs{position:absolute}
.serif{font-family:"PT Serif",serif}

/* header */
.site-header{left:0;top:0;width:1200px;height:116px;background:var(--white);border-bottom:1px solid #e6dcda}
.brand{left:107px;top:28px;display:flex;align-items:center;gap:10px}
.brand-mark{width:14px;height:14px;border:1.5px solid var(--ink);border-radius:50%}
.brand-name{font-family:"PT Serif",serif;font-size:34px;color:var(--ink)}
.nav a{position:absolute;top:48px;font-size:14px;color:var(--ink);text-decoration:none;transform:translateX(-50%)}
.nav .active::before,.nav .active::after{content:"";position:absolute;left:-18px;right:-18px;height:2px;background:var(--accent)}
.nav .active::before{top:-48px}
.nav .active::after{top:66px}
.search{left:1076px;top:52px}

/* hero */
.hero{left:0;top:116px;width:1200px;height:611px;background:linear-gradient(100deg,var(--hero-b) 0%,var(--hero-a) 45%,#9a9697 70%,#7d7b7c 100%)}
.hero-title{left:107px;top:223px;font-size:41px;line-height:46.5px;color:var(--white);width:315px}
.hero-text{left:107px;top:434px;font-size:14px;line-height:25px;color:var(--white);width:380px}
.follow{left:108px;top:508px;font-size:12px;color:var(--white)}
.social-hero span{position:absolute;top:535px;width:42px;height:42px;border:1.5px solid var(--white);border-radius:50%}
.social-hero span::after{content:"";position:absolute;left:17px;top:17px;width:6px;height:6px;border-radius:50%;background:var(--white)}
.learn{left:108px;top:673px;width:255px;height:54px;border:1px solid var(--white);border-bottom:none;color:var(--white);font-family:"PT Serif",serif;font-size:11px;padding:21px 0 0 24px;letter-spacing:.3px}
.learn svg{position:absolute;right:18px;top:23px}

/* about */
.about-title{right:654px;top:938px;font-size:31px;text-align:right}
.about-text{left:140px;width:406px;top:992px;font-size:13.5px;line-height:23.5px;text-align:right;color:var(--ink-soft)}
.about-photo{left:599px;top:859px;width:493px;height:310px;background:linear-gradient(135deg,#d8d5d0,#a9a59c 55%,#7e7a70)}
.deco{background:var(--dots);opacity:.12}

/* projects */
.kicker{font-size:12px;color:var(--ink-soft)}
.proj-title{left:116px;top:1338px;font-size:28px}
.tile{position:absolute}

/* testimonial */
.quote-box{left:124px;top:1992px;width:950px;height:380px;border:1.5px solid var(--line)}
.quote{left:124px;width:950px;top:2118px;font-size:20px;line-height:33px;text-align:center}
.author{left:124px;width:950px;top:2221px;font-size:16px;text-align:center}

/* contact */
.h-small{font-size:12px;color:var(--ink-soft)}
.h-serif{font-family:"PT Serif",serif;font-size:19px}
.small{font-size:12px;line-height:20px;color:var(--ink-soft)}
.field{position:absolute;border-bottom:1.5px solid var(--line);height:26px;font-size:11px;color:var(--ink-soft)}
.send{left:349px;top:2889px;width:129px;height:38px;border:1.5px solid var(--line);font-size:11px;text-align:center;line-height:35px}

/* footer */
.f-head{font-family:"PT Serif",serif;font-size:18px;top:3098px}
.f-list{top:3139px;font-size:12.5px;line-height:30px;list-style:none;color:var(--ink-soft)}
.news-input{left:772px;top:3171px;width:300px;height:40px;border:1.5px solid var(--accent);font-size:12px;padding:12px 0 0 12px;color:var(--ink-soft)}
.news-btn{left:987px;top:3171px;width:85px;height:40px;background:#261818}
.news-btn svg{position:absolute;left:32px;top:16px}
.f-social{left:122px;top:3380px;display:flex;gap:19px}
.f-social span{width:12px;height:12px;border-radius:50%;background:var(--ink)}
.copy{right:126px;top:3376px;font-size:12px;color:var(--ink-soft)}
</style>
</head>
<body>

<header class="abs site-header">
  <div class="abs brand"><span class="brand-mark"></span><span class="brand-name">Lumaform</span></div>
  <nav class="nav">
    <a class="active" style="left:551px">Home</a>
    <a style="left:640px">About</a>
    <a style="left:729px">Services</a>
    <a style="left:827px">Pricing</a>
    <a style="left:922px">Gallery</a>
    <a style="left:1014px">Contact</a>
  </nav>
  <svg class="abs search" width="12" height="12" viewBox="0 0 12 12"><circle cx="5" cy="5" r="3.6" fill="none" stroke="#2f2424" stroke-width="1.8"/><line x1="7.6" y1="7.6" x2="11" y2="11" stroke="#2f2424" stroke-width="1.8"/></svg>
</header>

<section class="abs hero" role="img" aria-label="Bright Scandinavian bedroom with pink bedding, shelving and a grey lounge chair"></section>
<h1 class="abs hero-title serif" style="font-weight:400">Make your home<br>a piece of art.<br>Inspired by great<br>design.</h1>
<p class="abs hero-text">Lorem ipsum dolor sit amet, consectetur adipisicing elit, sed do eiusmod</p>
<p class="abs follow">Follow Us</p>
<div class="social-hero">
  <span style="left:108px"></span><span style="left:161px"></span><span style="left:214px"></span><span style="left:268px"></span>
</div>
<div class="abs learn">LEARN MORE
  <svg width="16" height="8" viewBox="0 0 16 8"><line x1="0" y1="4" x2="14" y2="4" stroke="#fff" stroke-width="1.3"/><path d="M11 1l3 3-3 3" fill="none" stroke="#fff" stroke-width="1.3"/></svg>
</div>

<h2 class="abs about-title serif" style="font-weight:400">About Lumaform</h2>
<p class="abs about-text">Lumaform AS is working on the development of interior environments for private, corporate and public institutions. Finding the optimal solutions for a project, whether it is a room...</p>
<div class="abs deco" style="left:979px;top:1063px;width:142px;height:136px"></div>
<div class="abs about-photo" role="img" aria-label="Open coworking space with plants and lounge seating"></div>

<div class="abs deco" style="left:0;top:1338px;width:62px;height:150px;clip-path:polygon(0 0,100% 20%,0 100%)"></div>
<p class="abs kicker" style="left:116px;top:1312px">The best decoration trends in the world.</p>
<h2 class="abs proj-title serif" style="font-weight:400">Recent Projects</h2>
<div class="tile" style="left:118px;top:1402px;width:307px;height:225px;background:linear-gradient(160deg,#8a6d4a,#3b2f25 60%,#c9a26a)" role="img" aria-label="Round living room with dark chairs and warm wood floor"></div>
<div class="tile" style="left:448px;top:1402px;width:307px;height:225px;background:linear-gradient(120deg,#e4e6ea,#c5c9cf 60%,#6f6a66)" role="img" aria-label="White hall with spiral staircase and tall windows"></div>
<div class="tile" style="left:779px;top:1402px;width:307px;height:474px;background:linear-gradient(180deg,#dcd6d0,#b8a898 45%,#a8a7a6)" role="img" aria-label="Modern living room with grey sofa and wood media wall"></div>
<div class="tile" style="left:118px;top:1651px;width:307px;height:225px;background:linear-gradient(120deg,#f1efee,#d9d5d4 60%,#c8a8ad)" role="img" aria-label="Airy bedroom with sheer curtains and pink bedding"></div>
<div class="tile" style="left:448px;top:1651px;width:307px;height:225px;background:linear-gradient(90deg,#efefed 0%,#d8d4cf 55%,#1e1e1e 62%,#2f3b44 100%)" role="img" aria-label="Study corner with pendant lights and patterned rug"></div>

<div class="abs deco" style="left:1140px;top:1958px;width:60px;height:150px;clip-path:polygon(100% 0,0 40%,100% 100%)"></div>
<div class="abs quote-box"></div>
<p class="abs quote serif">Lorem ipsum dolor sit amet, consectetur<br>adipisicing elit, sed do eiusmod tempor</p>
<p class="abs author serif">- Ingrid Holm</p>

<div class="abs deco" style="left:0;top:2570px;width:72px;height:155px;clip-path:polygon(0 0,100% 70%,0 100%)"></div>
<p class="abs h-small" style="left:108px;top:2503px">Just Nearby</p>
<h3 class="abs h-serif" style="left:108px;top:2524px;font-weight:400">Location</h3>
<p class="abs small" style="left:108px;top:2563px;width:180px">Lumaform AS v / Ragna Tvedtholm Strandveien 14, 3480 Filtvet</p>
<p class="abs h-small" style="left:108px;top:2693px">Talk to</p>
<h3 class="abs h-serif" style="left:108px;top:2714px;font-weight:400">Our Experts</h3>
<p class="abs small" style="left:108px;top:2754px">Email: post@lumaform-example.no<br>Phone: +47 400 12 345</p>

<p class="abs h-small" style="left:349px;top:2503px">Get in touch</p>
<h3 class="abs h-serif" style="left:349px;top:2524px;font-weight:400">Say Hello</h3>
<p class="abs small" style="left:349px;top:2563px;width:740px;font-size:11.5px">Lorem ipsum dolor sit amet, consectetur adipisicing elit, sed do eiusmod tempor incididunt ut labore et dolore magna aliqua. Ut enim ad minim veniam quis nostrud exercitation.</p>
<div class="field" style="left:349px;top:2631px;width:224px">Your Name*</div>
<div class="field" style="left:597px;top:2631px;width:222px">Your Age*</div>
<div class="field" style="left:844px;top:2631px;width:248px">Email Address*</div>
<div class="field" style="left:349px;top:2695px;width:224px">Your Phone*</div>
<div class="field" style="left:597px;top:2695px;width:222px">Company Name (Optional)*</div>
<div class="field" style="left:844px;top:2695px;width:248px">Subject*</div>
<div class="field" style="left:349px;top:2765px;width:743px;height:98px">Message</div>
<div class="abs send">Send Message</div>

<h4 class="abs f-head" style="left:122px;font-weight:400">Navigation</h4>
<ul class="abs f-list" style="left:122px"><li>Home</li><li>About Lumaform</li><li>Services</li><li>Pricing</li><li>Latest Works</li></ul>
<h4 class="abs f-head" style="left:284px;font-weight:400">Quick Links</h4>
<ul class="abs f-list" style="left:284px"><li>Contact</li><li>Terms</li><li>Privacy Policy</li><li>Sitemap</li></ul>
<h4 class="abs f-head" style="left:447px;font-weight:400">Get in touch</h4>
<p class="abs small" style="left:447px;top:3138px;width:240px;line-height:20px">Address: Lumaform AS v / Ragna Tvedtholm Strandveien 14, 3480 Filtvet</p>
<p class="abs small" style="left:447px;top:3205px">Phone: +47 400 12 345</p>
<p class="abs small" style="left:447px;top:3235px">Email: post@lumaform-example.no</p>
<h4 class="abs f-head" style="left:772px;font-weight:400">Newsletter</h4>
<p class="abs small" style="left:772px;top:3130px">Get our latest news right in your mailbox</p>
<div class="abs news-input">Email</div>
<div class="abs news-btn"><svg width="18" height="8" viewBox="0 0 18 8"><line x1="0" y1="4" x2="16" y2="4" stroke="#fff" stroke-width="1.4"/><path d="M13 1l3 3-3 3" fill="none" stroke="#fff" stroke-width="1.4"/></svg></div>

<div class="abs deco" style="left:1142px;top:3200px;width:58px;height:145px;clip-path:polygon(100% 0,0 80%,100% 100%)"></div>
<div class="abs f-social" aria-label="Social links"><span></span><span></span><span></span><span></span><span></span><span></span></div>
<p class="abs copy">© 2020 Lumaform. All rights reserved.</p>

</body>
</html>
```